Business Card Design

My business will be called TB Joinery & Renovations. I am a liscenced carpentar who specialises in renovations/alterations/refurbishments and maintenance. I have experience in all types of Carpentry tho. I also have experience in tiling, painting and concrete which obviously gives me an edge in the refurbishment market for building. But i am not liscenced in these trades. I pride myself on being an honest and very reliable. There are alot of tradesman where i live who are not reliable so i really want to let the community know they can trust me and that i am willing to do all types of work.
I would like to see design and is not over the top but uses earthy/modern colours which presents a down to earth message.

I would really like to communicate diversity, reliabilty and quality work.

I have attached a couple of concepts i have come up with PaperKite, These may aid you.

Industry/Entity Type

Painting

Contact Information for Business Card

Name: Dean Wolworth
Email: dean.wolw@postlark.net
Ph: 0418529364

Requirements
Must have
• Licence No: 318827K

```html
<!DOCTYPE html>
<html lang="en">
<head>
<meta charset="utf-8">
<title>TB Joinery &amp; Renovations — Business Card</title>
<link rel="stylesheet" href="https://fonts.googleapis.com/css2?family=Michroma&family=Russo+One&display=swap">
<style>
  :root {
    --page: #e9e7e4;
    --card-black: #0e0e0e;
    --card-white: #f4f4f4;
    --brand-red: #e8180f;
    --deep-red: #5a0805;
    --ink: #111111;
    --paper-text: #f2f2f2;
    --rule-grey: #3a3a3a;
  }
  * { margin: 0; padding: 0; box-sizing: border-box; }
  html, body {
    width: 1132px;
    height: 1200px;
    overflow: hidden;
    background: var(--page);
  }
  .canvas {
    position: relative;
    width: 1132px;
    height: 1200px;
  }
  .card {
    position: absolute;
    left: 86px;
    width: 960px;
    height: 542px;
    border-radius: 32px;
    overflow: hidden;
    background: var(--card-black);
    box-shadow: 0 6px 18px rgba(0,0,0,0.25);
  }
  .card--front { top: 31px; }
  .card--back { top: 623px; }

  /* Front */
  .front-top {
    position: absolute;
    left: 0; top: 0;
    width: 100%;
    height: 256px;
    background: linear-gradient(180deg, #ffffff 0%, var(--card-white) 100%);
    border-bottom: 3px solid var(--rule-grey);
  }
  .front-glow {
    position: absolute;
    left: 130px; top: 259px;
    width: 420px; height: 5px;
    background: linear-gradient(90deg, rgba(232,24,15,0) 0%, var(--brand-red) 60%, var(--brand-red) 100%);
  }
  .brand-name {
    position: absolute;
    font-family: "Russo One", sans-serif;
    color: var(--brand-red);
    text-align: center;
    letter-spacing: 1px;
    line-height: 1;
  }
  .brand-name--front {
    left: 0; right: 0; top: 80px;
    font-size: 54px;
    color: var(--ink);
  }
  .brand-name--back {
    left: 0; right: 0; top: 200px;
    font-size: 60px;
  }
  .name-tab {
    position: absolute;
    left: 496px; top: 262px;
    width: 415px; height: 91px;
  }
  .name-tab svg { position: absolute; inset: 0; }
  .holder-name {
    position: absolute;
    left: 0; right: 0; top: 30px;
    text-align: center;
    font-family: "Russo One", sans-serif;
    font-size: 27px;
    color: var(--ink);
    letter-spacing: 1px;
  }
  .services {
    position: absolute;
    left: 35px; top: 428px;
    list-style: none;
    font-family: "Michroma", sans-serif;
    font-size: 14px;
    line-height: 25px;
    letter-spacing: 2px;
    color: var(--paper-text);
  }
  .contacts {
    position: absolute;
    right: 28px; top: 438px;
    list-style: none;
    font-family: "Michroma", sans-serif;
    font-size: 15px;
    line-height: 26px;
    letter-spacing: 2px;
    color: var(--paper-text);
    text-align: right;
  }
  .contacts li { display: flex; justify-content: flex-end; align-items: center; gap: 8px; }
  .contacts .icon { width: 12px; height: 12px; }
  .contacts .icon-gap { width: 12px; }

  /* Back */
  .email-tab {
    position: absolute;
    left: 518px; top: 459px;
    width: 442px; height: 83px;
  }
  .email-tab svg { position: absolute; inset: 0; }
  .back-glow {
    position: absolute;
    left: 0; top: 536px;
    width: 540px; height: 6px;
    background: linear-gradient(90deg, rgba(232,24,15,0) 0%, var(--brand-red) 100%);
  }
  .back-email {
    position: absolute;
    left: 0; right: 40px; top: 24px;
    text-align: center;
    font-family: "Michroma", sans-serif;
    font-size: 17px;
    letter-spacing: 2px;
    color: var(--ink);
  }
</style>
</head>
<body>
<main class="canvas">

  <section class="card card--front" aria-label="Business card front">
    <div class="front-top"></div>
    <div class="front-glow"></div>
    <p class="brand-name brand-name--front">TB Joinery &amp; Renovations</p>

    <div class="name-tab">
      <svg width="415" height="91" viewBox="0 0 415 91" aria-hidden="true">
        <defs>
          <linearGradient id="nameTabFill" x1="0" y1="0" x2="1" y2="0">
            <stop offset="0" stop-color="#e8180f"/>
            <stop offset="0.55" stop-color="#e8180f"/>
            <stop offset="1" stop-color="#5a0805"/>
          </linearGradient>
        </defs>
        <path d="M0 0 H415 L396 72 Q391 91 372 91 H40 Q22 91 18 74 Z" fill="url(#nameTabFill)"/>
      </svg>
      <p class="holder-name">Dean Wolworth</p>
    </div>

    <ul class="services">
      <li>Carpentry &amp; All Building Services</li>
      <li>Renovations</li>
      <li>Maintenance</li>
      <li>General Repairs</li>
    </ul>

    <ul class="contacts">
      <li>0418 529 364
        <svg class="icon" viewBox="0 0 12 12" aria-hidden="true">
          <path d="M2.5 1 L4.5 1 L5.3 3.6 L4 4.6 Q5 7 7.4 8 L8.4 6.7 L11 7.5 L11 9.5 Q10.5 11 9 11 Q2 10 1 3 Q1 1.5 2.5 1 Z" fill="#e8180f"/>
        </svg>
      </li>
      <li>dean.wolw@postlark.net
        <svg class="icon" viewBox="0 0 12 12" aria-hidden="true">
          <circle cx="6" cy="6" r="5" fill="none" stroke="#e8180f" stroke-width="1.6"/>
          <circle cx="6" cy="6" r="1.8" fill="#e8180f"/>
        </svg>
      </li>
      <li>Lic No : 318827K <span class="icon-gap"></span></li>
    </ul>
  </section>

  <section class="card card--back" aria-label="Business card back">
    <p class="brand-name brand-name--back">TB Joinery &amp; Renovations</p>
    <div class="back-glow"></div>
    <div class="email-tab">
      <svg width="442" height="83" viewBox="0 0 442 83" aria-hidden="true">
        <defs>
          <linearGradient id="emailTabFill" x1="0" y1="0" x2="1" y2="0">
            <stop offset="0" stop-color="#e8180f"/>
            <stop offset="0.6" stop-color="#e8180f"/>
            <stop offset="1" stop-color="#7a0c07"/>
          </linearGradient>
        </defs>
        <path d="M0 83 L18 14 Q22 0 40 0 H370 Q388 0 393 14 L410 83 Z" fill="url(#emailTabFill)"/>
      </svg>
      <p class="back-email">dean.wolw@postlark.net</p>
    </div>
  </section>

</main>
</body>
</html>
```